Kestrel Business Accountants , logo & business card design

I am a business consultant & accountant , servicing a range of small business clients , providing business & taxation advice.
I am looking for a logo & business card design that is not traditional accounting style.
Something colorful & innovative would be good.
Target Market(s)
Small businesses in their growth stage
Industry/Entity Type
Business Consultant
Contact Information for Business Card
Kestrel Business Accountants Pty Ltd
Miles Hartley CPA
Director
Ph: 0413 8064 91
Email : kestrel@pallinet.com.au
On reverse of card:
"Kestrel Sight for your Business"
Business Consulting
Taxation
Superannuation
Logo styles of interest
Abstract Logo
Wordmark Logo
Look and feel

```html
<!DOCTYPE html>
<html lang="en">
<head>
<meta charset="utf-8">
<title>Kestrel Business Accountants – Business Card</title>
<link href="https://fonts.googleapis.com/css2?family=Arimo:ital,wght@0,400;0,700;1,400&display=swap" rel="stylesheet">
<style>
  :root {
    --page-bg: #3a3a3a;
    --card-bg: #2e2e30;
    --card-bg-light: #3a3a3c;
    --text-light: #e6e6e6;
    --text-soft: #c9c9c9;
    --brand-blue: #1f7fc0;
    --silver: #d4d4d4;
    --art-tone-a: #4a4a4e;
    --art-tone-b: #3c3c40;
  }
  * { box-sizing: border-box; margin: 0; padding: 0; }
  html, body {
    width: 1200px; height: 990px; overflow: hidden;
    background: var(--page-bg);
    font-family: "Arimo", Arial, sans-serif;
  }
  .sheet {
    width: 1200px; height: 990px;
    display: flex; flex-direction: column; align-items: center; justify-content: center;
    gap: 60px;
  }
  .card {
    position: relative;
    width: 720px; height: 410px;
    border-radius: 26px;
    background: linear-gradient(160deg, var(--card-bg-light), var(--card-bg) 60%);
    box-shadow: 0 10px 30px rgba(0,0,0,.45);
    overflow: hidden;
    color: var(--text-light);
  }
  /* front */
  .card-header {
    position: absolute; left: 40px; top: 40px;
    display: flex; align-items: baseline; gap: 40px;
  }
  .brand { display: flex; align-items: center; gap: 12px; }
  .brand-dot { width: 18px; height: 18px; border-radius: 50%; background: var(--brand-blue); }
  .brand-name { font-size: 38px; font-weight: 700; color: var(--brand-blue); }
  .brand-tagline { font-size: 24px; letter-spacing: .5px; color: var(--text-light); }
  .person { position: absolute; left: 40px; top: 165px; }
  .person-name { font-size: 34px; color: var(--text-light); }
  .person-role { font-size: 28px; color: var(--text-soft); margin-top: 6px; }
  .contact { position: absolute; left: 40px; top: 285px; list-style: none; }
  .contact li {
    display: flex; align-items: center; gap: 14px;
    font-size: 24px; color: var(--text-light); margin-bottom: 12px;
  }
  .contact svg { width: 26px; height: 22px; }
  .growth-art {
    position: absolute; right: 36px; top: 120px;
    width: 290px; height: 250px; border-radius: 14px;
    background: linear-gradient(160deg, var(--art-tone-a), var(--art-tone-b));
  }
  /* back */
  .slogan { position: absolute; right: 44px; top: 40px; text-align: right; }
  .slogan-quote { font-size: 24px; font-style: italic; color: var(--text-light); }
  .slogan-services { font-size: 18px; color: var(--text-soft); margin-top: 6px; letter-spacing: .3px; }
  .back-band {
    position: absolute; left: 0; right: 0; top: 190px; height: 2px;
    background: linear-gradient(90deg, transparent, rgba(255,255,255,.12), transparent);
  }
  .back-name {
    position: absolute; right: 44px; bottom: 34px;
    font-size: 96px; color: var(--silver); letter-spacing: 1px;
  }
</style>
</head>
<body>
<main class="sheet">
  <section class="card card-front">
    <header class="card-header">
      <div class="brand">
        <span class="brand-dot"></span>
        <span class="brand-name">Kestrel</span>
      </div>
      <p class="brand-tagline">Business Accountants</p>
    </header>
    <div class="person">
      <p class="person-name">Miles Hartley</p>
      <p class="person-role">CPA Director</p>
    </div>
    <ul class="contact">
      <li>
        <svg viewBox="0 0 26 22" aria-hidden="true"><circle cx="11" cy="11" r="9.5" fill="none" stroke="#cfcfcf" stroke-width="1.5"/><path d="M8 6c-1 2 0 6 4 9 1 1 2 1 3 0l-1.5-2-1.5 1c-1.5-1-2.5-3-2.5-4l1.5-1L9.5 6z" fill="#cfcfcf"/><text x="20" y="16" fill="#cfcfcf" font-size="12">:</text></svg>
        <span>0413 8064 91</span>
      </li>
      <li>
        <svg viewBox="0 0 26 22" aria-hidden="true"><rect x="1" y="4" width="18" height="13" fill="#cfcfcf"/><path d="M1 4l9 7 9-7" fill="none" stroke="#2e2e30" stroke-width="1.4"/><text x="20" y="16" fill="#cfcfcf" font-size="12">:</text></svg>
        <span>kestrel@pallinet.com.au</span>
      </li>
    </ul>
    <div class="growth-art" role="img" aria-label="Illustration of colourful curved upward arrows symbolising business growth"></div>
  </section>

  <section class="card card-back">
    <div class="slogan">
      <p class="slogan-quote">"Kestrel Sight for your Business"</p>
      <p class="slogan-services">Business Consulting Taxation Superannuation</p>
    </div>
    <div class="back-band"></div>
    <p class="back-name">Kestrel</p>
  </section>
</main>
</body>
</html>
```